Business Cards for a start up company

We are looking for a business card design for a start up company based in Ohio. The logo is attached. We are a healthcare company. We are open to all designs but want something professional but fun; creative, not boring

Industry/Entity Type

Healthcare

```html
<!DOCTYPE html>
<html lang="en">
<head>
<meta charset="utf-8">
<title>Bright Bridge Care — Business Cards</title>
<link rel="stylesheet" href="https://fonts.googleapis.com/css2?family=Exo+2:wght@400;600;700&display=swap">
<style>
  :root {
    --navy: #23235e;
    --green: #8dc63f;
    --sky: #1fb5e3;
    --white: #ffffff;
    --paper: #f1f1f3;
    --backdrop: #e4e5e8;
    --ink-soft: #d9dbe8;
  }
  * { box-sizing: border-box; margin: 0; padding: 0; }
  html, body {
    width: 1200px; height: 1018px; overflow: hidden;
    background: var(--backdrop);
    font-family: "Exo 2", sans-serif;
  }
  .sheet {
    width: 1200px; height: 1018px;
    display: flex; flex-direction: column; align-items: center; justify-content: center;
    gap: 60px;
  }
  .card {
    position: relative;
    width: 700px; height: 400px;
    overflow: hidden;
    box-shadow: 0 10px 30px rgba(0,0,0,.18);
  }

  /* Back: brand side */
  .card--brand { background: var(--navy); }
  .brand-field {
    position: absolute; left: 0; top: 0;
    width: 440px; height: 400px;
    background: linear-gradient(180deg, var(--white), var(--paper));
    border-radius: 0 0 200px 0;
    display: flex; align-items: center; justify-content: center;
  }
  .brand-name {
    display: flex; align-items: center; gap: 14px;
    color: var(--navy); font-weight: 600; font-size: 30px;
  }
  .brand-dot {
    width: 40px; height: 40px; border-radius: 50%;
    background: var(--sky);
  }
  .web-strip {
    position: absolute; right: 24px; bottom: 0;
    width: 58px; height: 250px;
    background: var(--green);
    display: flex; align-items: center; justify-content: center;
  }
  .web-strip span {
    transform: rotate(-90deg);
    white-space: nowrap;
    color: var(--navy); font-size: 16px; letter-spacing: .5px;
  }

  /* Front: contact side */
  .card--contact { background: var(--white); }
  .brand-mark-area {
    position: absolute; left: 36px; top: 60px;
    display: flex; align-items: center; gap: 16px;
    color: var(--navy); font-weight: 600; font-size: 28px;
  }
  .brand-mark-area .brand-dot { width: 56px; height: 56px; background: var(--green); }
  .accent-arc {
    position: absolute; left: 262px; top: 130px;
    width: 470px; height: 300px;
    border: 4px solid var(--green);
    border-radius: 150px 0 0 0;
  }
  .contact-panel {
    position: absolute; left: 278px; top: 146px;
    width: 422px; height: 254px;
    background: var(--navy);
    border-radius: 140px 0 0 0;
    padding: 22px 30px 0 0;
    color: var(--white);
    text-align: right;
  }
  .contact-panel .rule {
    height: 2px; background: var(--white);
    width: 300px; margin-left: auto; margin-bottom: 10px;
  }
  .person-name { font-size: 22px; font-weight: 700; letter-spacing: 1.5px; line-height: 1.1; }
  .person-role { font-size: 14px; letter-spacing: 1.5px; margin-bottom: 12px; }
  .contact-list { list-style: none; display: flex; flex-direction: column; gap: 6px; }
  .contact-list li {
    display: flex; align-items: center; justify-content: flex-end; gap: 8px;
    font-size: 12px; color: var(--ink-soft);
  }
  .contact-list svg { width: 18px; height: 18px; flex: none; }
</style>
</head>
<body>
<main class="sheet">

  <section class="card card--brand" aria-label="Business card, brand side">
    <div class="brand-field">
      <div class="brand-name"><span class="brand-dot"></span>Bright Bridge Care</div>
    </div>
    <div class="web-strip"><span>www.brightbridgecare.com</span></div>
  </section>

  <section class="card card--contact" aria-label="Business card, contact side">
    <div class="brand-mark-area"><span class="brand-dot"></span>Bright Bridge Care</div>
    <div class="accent-arc"></div>
    <div class="contact-panel">
      <div class="rule"></div>
      <p class="person-name">DANIEL REYES</p>
      <p class="person-role">GENERAL MANAGER</p>
      <ul class="contact-list">
        <li>014 555 0192
          <svg viewBox="0 0 18 18" fill="none" stroke="#fff" stroke-width="1.3"><circle cx="9" cy="9" r="8"/><path d="M6 5l2 2-1 1.2c.6 1.3 1.5 2.2 2.8 2.8L11 10l2 2-1.3 1.2C8.5 13 5 9.5 4.8 6.3z" fill="#fff" stroke="none"/></svg></li>
        <li>014 555 0193
          <svg viewBox="0 0 18 18" fill="none" stroke="#fff" stroke-width="1.3"><circle cx="9" cy="9" r="8"/><rect x="6.5" y="4.5" width="5" height="9" rx="1"/></svg></li>
        <li>014 555 0194
          <svg viewBox="0 0 18 18" fill="none" stroke="#fff" stroke-width="1.3"><circle cx="9" cy="9" r="8"/><rect x="5" y="7" width="8" height="5"/><path d="M6.5 7V4.5h5V7"/></svg></li>
        <li>hello@brightbridge.care
          <svg viewBox="0 0 18 18" fill="none" stroke="#fff" stroke-width="1.3"><circle cx="9" cy="9" r="8"/><rect x="5" y="6" width="8" height="6"/><path d="M5 6l4 3 4-3"/></svg></li>
        <li>www.brightbridgecare.com
          <svg viewBox="0 0 18 18" fill="none" stroke="#fff" stroke-width="1.3"><circle cx="9" cy="9" r="8"/><circle cx="9" cy="9" r="4"/><path d="M5 9h8M9 5c-1.5 2.5-1.5 5.5 0 8M9 5c1.5 2.5 1.5 5.5 0 8"/></svg></li>
        <li>42 Maple Road, 3rd Floor, Suite W
          <svg viewBox="0 0 18 18" fill="none" stroke="#fff" stroke-width="1.3"><circle cx="9" cy="9" r="8"/><path d="M9 14s-3.5-3.6-3.5-6a3.5 3.5 0 0 1 7 0c0 2.4-3.5 6-3.5 6z"/><circle cx="9" cy="8" r="1.2" fill="#fff"/></svg></li>
      </ul>
    </div>
  </section>

</main>
</body>
</html>
```